Tree Pruning Website

We need a website for a tree Arborist, pruning company called Hollow Ridge Groundcare. We look after all types of trees, knock down trees and prune trees. Our target market is from domestic clients to government clients and everything in between.

We would like to see the use of our main colours which are orange and green

We are not looking forward in seeing a template that we have seen before but a unique template. We have designed 5 templates ourselves and we wish for the design community to take our designs to the next level.

We have also designed a template for things that **we are not** looking for (Version 4)

To make it fair for everyone, we are also not giving out any participation payments as we have had. One winner will take all of the payment!!!

I Have attached a image of the designs and a image of a tree.

We are just looking at the PSD file been developed. We have our own team who can slice the image up into a HTML format.

Target Market(s)

Everyone who needs to cut down a tree

Industry/Entity Type

Government

Requirements
Must have
• Logo on front page
A List of our services
jQuery slider on page
Phone Number on every page

```html
<!DOCTYPE html>
<html lang="en">
<head>
<meta charset="utf-8">
<title>Hollow Ridge Groundcare — Tree Pruning Perth</title>
<link href="https://fonts.googleapis.com/css2?family=Questrial&family=PT+Sans:wght@400;700&family=Schoolbell&display=swap" rel="stylesheet">
<style>
:root{
  --canvas:#dcdcdc;
  --header:#dcedb4;
  --green:#8ab92a;
  --green-dark:#5f8f14;
  --green-light:#b4d658;
  --leaf:#6aa51f;
  --orange:#d9600f;
  --orange-deep:#c9510a;
  --text:#3a3a3a;
  --muted:#6b6b6b;
  --paper:#f4f4f2;
  --white:#fff;
}
*{box-sizing:border-box;margin:0;padding:0}
html,body{width:1200px;height:900px;overflow:hidden}
body{background:var(--canvas);font-family:"PT Sans",sans-serif;color:var(--text);position:relative}
.page{position:absolute;left:313px;top:11px;width:574px;height:878px;background:var(--paper);overflow:hidden}
.abs{position:absolute}

/* header */
.site-header{left:0;top:0;width:574px;height:71px;background:linear-gradient(#e3f1c1,var(--header))}
.brand{left:50px;top:14px;display:flex;align-items:center;gap:8px}
.brand-dot{width:30px;height:30px;border-radius:50%;background:var(--leaf)}
.brand-name{font-family:"Questrial",sans-serif;color:var(--leaf);font-size:17px;line-height:19px}
.phone-badge{left:414px;top:11px;width:114px;height:22px;background:linear-gradient(90deg,var(--orange-deep),#ee8a1e);color:var(--white);font-family:"PT Sans",sans-serif;font-weight:700;font-size:12px;display:flex;align-items:center;gap:5px;padding-left:15px;box-shadow:2px 2px 3px rgba(0,0,0,.2)}
.main-nav{left:237px;top:41px;display:flex;gap:0;align-items:center}
.main-nav a{font-size:8px;font-weight:700;color:#222;text-decoration:none;padding:4px 7px}
.main-nav a.is-active{background:linear-gradient(#b9dc62,var(--green));border-radius:3px;padding:4px 9px;margin-right:2px}

/* slider */
.hero{left:0;top:71px;width:574px;height:214px;background:linear-gradient(120deg,#6e5a3e 0%,#8a7b5c 30%,#4f7fc2 55%,#2d3f60 80%,#e0e0e0 100%)}
.hero-line{background:var(--white);font-family:"Questrial",sans-serif;color:#555;white-space:nowrap;padding:0 3px}
.hero-line strong{font-weight:700;font-family:"PT Sans",sans-serif}
.hero-line.one{left:49px;top:26px;font-size:18px;height:24px;line-height:24px}
.hero-line.one strong{color:var(--leaf);font-size:20px}
.hero-line.two{left:49px;top:52px;font-size:15px;height:24px;line-height:24px}
.hero-line.two strong{color:var(--orange);font-size:16px}
.hero-arrow{top:92px}
.hero-dots{left:278px;top:197px;display:flex;gap:4px}
.hero-dots span{width:6px;height:6px;border-radius:50%;background:#ddd}
.hero-dots span:first-child{background:var(--green)}

/* services */
.service{width:114px;height:169px;top:307px;background:linear-gradient(#a6cf3c,var(--green));border-radius:2px;box-shadow:0 1px 2px rgba(0,0,0,.25);text-align:center}
.service h3{font-family:"Questrial",sans-serif;font-weight:400;color:#3c4d10;font-size:15px;height:25px;line-height:26px;background:linear-gradient(#c8e47a,#9fca35)}
.service .thumb{margin:3px 4px 0;height:54px;border:1px solid #e8f3c8}
.service h4{font-size:9px;font-weight:700;color:#222;margin-top:8px}
.service p{font-size:7.4px;line-height:8.6px;color:var(--white);margin:7px 6px 0}
.service::after{content:"";position:absolute;left:50px;bottom:-6px;border:7px solid transparent;border-bottom:0;border-top-color:var(--green)}
.read-more{font-family:"Schoolbell",cursive;font-size:10px;color:#333;top:486px;width:114px;text-align:center;text-decoration:underline}

/* intro */
.intro{left:0;top:528px;width:574px;text-align:center}
.intro h2{font-family:"Questrial",sans-serif;font-weight:400;color:var(--green);font-size:15px}
.intro .motto{font-family:"Questrial",sans-serif;color:var(--orange);font-size:10.5px;margin-top:1px}
.intro .lead{font-size:9.5px;color:#555;margin-top:8px}
.intro .copy{font-size:6.3px;line-height:10px;color:var(--muted);margin:1px 50px 0}
.intro .copy + .copy{margin-top:9px}

/* footer */
.site-footer{left:0;top:672px;width:574px;height:166px;background:linear-gradient(var(--orange-deep),var(--orange) 50%,var(--orange-deep))}
.contact{left:62px;top:24px;color:var(--white)}
.contact h3{font-family:"Questrial",sans-serif;font-weight:400;font-size:12px}
.contact .map{width:115px;height:46px;margin-top:3px;background:linear-gradient(#efe6d8,#e2d6c2);border:2px solid #f2a061}
.contact p{font-size:7px;line-height:8px;margin-top:6px}
.gallery{left:209px;top:29px;width:305px;height:114px;background:linear-gradient(#fff,#dcdcdc);border-radius:6px;box-shadow:0 2px 4px rgba(0,0,0,.3)}
.gallery-tab{left:6px;top:6px;width:71px;height:26px;background:linear-gradient(#c2e06a,var(--green));border-radius:4px 4px 0 0;font-family:"Questrial",sans-serif;font-size:15px;line-height:28px;text-align:center;color:#1f2b06}
.gallery-intro{left:88px;top:7px}
.gallery-intro h4{font-size:9px;font-weight:700;color:#222}
.gallery-intro p{font-size:6.5px;color:#555}
.gallery-thumb{top:42px;width:78px;height:64px;border-radius:6px}
.gallery-arrow{top:64px}

/* bottom bar */
.bottom-bar{left:0;top:838px;width:574px;height:40px;background:linear-gradient(#8bbd31,var(--leaf));text-align:center}
.bottom-nav{display:flex;justify-content:center;gap:0;margin-top:10px}
.bottom-nav a{font-size:6.5px;font-weight:700;color:#1b2a05;text-decoration:none;padding:0 6px}
.bottom-nav a.is-active{color:var(--white)}
.copyright{font-size:6.5px;color:#1b2a05;margin-top:4px}
</style>
</head>
<body>
<div class="page">

  <header class="site-header abs">
    <div class="brand abs">
      <span class="brand-dot"></span>
      <span class="brand-name">Hollow Ridge<br>Groundcare</span>
    </div>
    <div class="phone-badge abs">
      <svg width="9" height="11" viewBox="0 0 9 11"><rect x="1" y="0.5" width="7" height="10" rx="1" fill="none" stroke="#fff" stroke-width="1.2"/><rect x="3" y="8" width="3" height="1" fill="#fff"/></svg>
      08 7000 4821
    </div>
    <nav class="main-nav abs">
      <a class="is-active" href="#">Home</a>
      <a href="#">About Us</a>
      <a href="#">Our Services</a>
      <a href="#">Get A Quote</a>
      <a href="#">Our Work</a>
      <a href="#">Contact Us</a>
    </nav>
  </header>

  <section class="hero abs" role="img" aria-label="Photo of an arborist in a helmet cutting a large tree branch with a chainsaw against a blue sky">
    <div class="hero-line one abs"><strong>Hollow Ridge</strong> is the leading</div>
    <div class="hero-line two abs"><strong>TREE PURNING SERVICE</strong> located in Perth.</div>
    <svg class="hero-arrow abs" style="left:16px" width="20" height="30" viewBox="0 0 20 30"><path d="M16 2 L4 15 L16 28" fill="none" stroke="#fff" stroke-width="3"/></svg>
    <svg class="hero-arrow abs" style="left:538px" width="20" height="30" viewBox="0 0 20 30"><path d="M4 2 L16 15 L4 28" fill="none" stroke="#fff" stroke-width="3"/></svg>
    <div class="hero-dots abs"><span></span><span></span><span></span></div>
  </section>

  <article class="service abs" style="left:48px">
    <h3>Domestic</h3>
    <div class="thumb" role="img" aria-label="Photo of hedge shears trimming a garden hedge" style="background:linear-gradient(#4a6b9a,#4f8a2a)"></div>
    <h4>Lorem ipsum dolor sit</h4>
    <p>Consectetur adipiscing elit. Nulla lobortis consequat mauris, eget eleifend nunc viverra viverra. Ut ac risus odio. Aliquam pretium purus sed nulla feugiat blandit.</p>
  </article>
  <article class="service abs" style="left:170px">
    <h3>Commercial</h3>
    <div class="thumb" role="img" aria-label="Photo of an office building with trimmed trees in front" style="background:linear-gradient(#b9c3cc,#5e6e5a)"></div>
    <h4>Lorem ipsum dolor sit</h4>
    <p>Consectetur adipiscing elit. Nulla lobortis consequat mauris, eget eleifend nunc viverra viverra. Ut ac risus odio. Aliquam pretium purus sed nulla feugiat blandit.</p>
  </article>
  <article class="service abs" style="left:291px">
    <h3>Government</h3>
    <div class="thumb" role="img" aria-label="Photo of a formal hedge maze garden" style="background:linear-gradient(#7aa05a,#3f7a2a)"></div>
    <h4>Lorem ipsum dolor sit</h4>
    <p>Consectetur adipiscing elit. Nulla lobortis consequat mauris, eget eleifend nunc viverra viverra. Ut ac risus odio. Aliquam pretium purus sed nulla feugiat blandit.</p>
  </article>
  <article class="service abs" style="left:412px">
    <h3>Non profit</h3>
    <div class="thumb" role="img" aria-label="Photo of a gardener trimming a tall hedge" style="background:linear-gradient(#3d5a4a,#5a8a3a)"></div>
    <h4>Lorem ipsum dolor sit</h4>
    <p>Consectetur adipiscing elit. Nulla lobortis consequat mauris, eget eleifend nunc viverra viverra. Ut ac risus odio. Aliquam pretium purus sed nulla feugiat blandit.</p>
  </article>
  <a class="read-more abs" style="left:48px">Read More</a>
  <a class="read-more abs" style="left:170px">Read More</a>
  <a class="read-more abs" style="left:291px">Read More</a>
  <a class="read-more abs" style="left:412px">Read More</a>

  <section class="intro abs">
    <h2>Hollow Ridge is the leading tree purning service located in Perth.</h2>
    <p class="motto">Our motto is when you call, we guarantee to turn up and provide care to our customers.</p>
    <p class="lead">Lorem ipsum dolor sit amet, consectetur adipiscing elit. Nulla lobortis consequat mauris,</p>
    <p class="copy">eget eleifend nunc viverra viverra. Ut ac risus odio. Aliquam pretium purus sed nulla feugiat blandit. Cras vel libero ut lacus eleifend tempor. Phasellus eleifend, magna non tincidunt accumsan, justo arcu cursus ipsum, non porttitor sapien quam vel magna. Maecenas elit nisl, molestie nec dapibus nec.</p>
    <p class="copy">Aliquet a erat. Donec scelerisque lacus a libero suscipit auctor volutpat enim euismod. Mauris porta, lacus ut ullamcorper sodales, mauris tortor feugiat purus, nec aliquam neque purus ac metus. Nunc eleifend leo quis nisl hendrerit ultrices. Suspendisse quis feugiat elit. Fusce vitae dolor ac est tincidunt feugiat. Phasellus volutpat dui in sapien malesuada tempus placerat justo ultricies. Duis mollis ornare risus, ut consectetur mi tincidunt sit amet. Maecenas quis nibh ac orci tempus scelerisque ac et massa.</p>
  </section>

  <footer class="site-footer abs">
    <div class="contact abs">
      <h3>Contact Information</h3>
      <div class="map" role="img" aria-label="Street map showing the office location with a pin"></div>
      <p>14 Marlow Street<br>KENTWOOD, WA 6158</p>
      <p>Tel: 08 7000 4821<br>Fax: 08 7000 4830</p>
      <p>Email: email@hollowridgegroundcare.com</p>
    </div>
    <div class="gallery abs">
      <div class="gallery-tab abs">Gallery</div>
      <div class="gallery-intro abs">
        <h4>Lorem ipsum dolor sit amet,</h4>
        <p>eget eleifend nunc viverra viverra. Ut ac risus odio. Aliquam pretium purus</p>
      </div>
      <svg class="gallery-arrow abs" style="left:8px" width="12" height="16" viewBox="0 0 12 16"><path d="M11 1 L1 8 L11 15Z" fill="var(--green)"/></svg>
      <div class="gallery-thumb abs" style="left:28px;background:linear-gradient(#6b8a3a,#a34a3a)" role="img" aria-label="Photo of a worker pruning a shrub"></div>
      <div class="gallery-thumb abs" style="left:114px;background:linear-gradient(#7aa84a,#3f6a2a)" role="img" aria-label="Photo of a worker among tall green trees"></div>
      <div class="gallery-thumb abs" style="left:200px;background:linear-gradient(#9fc0e6,#6a5a3a)" role="img" aria-label="Photo of loppers cutting a branch against the sky"></div>
      <svg class="gallery-arrow abs" style="left:285px" width="12" height="16" viewBox="0 0 12 16"><path d="M1 1 L11 8 L1 15Z" fill="var(--green)"/></svg>
    </div>
  </footer>

  <div class="bottom-bar abs">
    <nav class="bottom-nav">
      <a class="is-active" href="#">Home</a>
      <a href="#">About Us</a>
      <a href="#">Our Services</a>
      <a href="#">Get A Quote</a>
      <a href="#">Our Work</a>
      <a href="#">Contact Us</a>
    </nav>
    <p class="copyright">Copyright Information comes here</p>
  </div>

</div>
</body>
</html>
```